Nordic Joinery Guild Wordpress Theme and newsletter template

We at the NJG are looking to start a Wordpress website and also send out a newsletter (web). We have just completed a Logo design project with ArtFlockly and we were so pleased with the results that we would like to see what the designers can come up with for a Wordpress theme and a template for an online newsletter. The theme has to support Icelandic letters. It also has to have a subscription option by email. We would need to have the option to add advertisement banners. The theme has to be easy to work with.
Below we have added a two websites for a example of what we are looking for: .
http://www.torvexhub.example/
http://www.brakkel.example/
The newsletter has to have a similar theme as the website and will be used with MS Publisher.

Attached is the new NJG logo.
Updates

Project Deadline Extended Reason: Not fully happy with the designs we have gotten so far. Would like to extend time to see if improvements can be made. Added Tuesday, June 16, 2015

Target Market(s)

Welding association members, welding and metalworking industry, suppliers in welding industry, International welding community, other national welding associations, welding education community

Industry/Entity Type

Welding

Number of Pages Required

3 page

Requirements
Must have
• The TKBÓ logo
• Icelandic letters
• email formpage
• Advertisement space/banners/buttons
• Easy to manage
• Compatible with Wordpress
Nice to have
• Welding pictures
• Nice graphics
Should not have
• Should not be dark and heavy set.

```html
<!DOCTYPE html>
<html lang="is">
<head>
<meta charset="utf-8">
<title>TKBÓ Welding</title>
<link rel="stylesheet" href="https://fonts.googleapis.com/css2?family=Source+Sans+3:wght@300;400;600;700&family=Arimo:wght@400;700&family=Questrial&display=swap">
<style>
:root{
  --blue:#1d8fc4;
  --blue-dark:#0f6a9c;
  --link-blue:#1a6f9e;
  --red:#c4161c;
  --red-dark:#9d1016;
  --sky:#e6f4fa;
  --text:#333;
  --muted:#666;
  --grey-band:#eeeeee;
  --footer-top:#555;
  --footer-bottom:#2a2a2a;
  --line:#d7d7d7;
}
*{box-sizing:border-box;margin:0;padding:0}
html,body{width:1200px;height:2323px;overflow:hidden}
body{position:relative;background:#fff;font-family:"Arimo",Arial,sans-serif;color:var(--text)}

/* header */
.site-header{position:absolute;left:0;top:0;width:1200px;height:98px;background:var(--sky)}
.brand{position:absolute;left:105px;top:26px;display:flex;align-items:center;gap:10px;font-family:"Source Sans 3",sans-serif;font-weight:700;font-size:30px;color:var(--red)}
.brand-mark{width:26px;height:26px;border-radius:50%;background:var(--blue)}
.main-nav{position:absolute;left:464px;top:0;height:98px;display:flex;font-family:"Arimo",sans-serif;font-size:13px;color:#222}
.main-nav a{display:flex;align-items:center;height:98px;padding:0 22px;text-decoration:none;color:inherit}
.main-nav a.current{background:#fff;border-top:4px solid var(--red);border-left:1px solid #ddd;border-right:1px solid #ddd;padding:0 20px;margin-right:1px}

/* hero */
.hero{position:absolute;left:0;top:98px;width:1200px;height:410px;overflow:hidden}
.hero-photo{position:absolute;left:440px;top:0;width:760px;height:410px;background:radial-gradient(ellipse at 45% 55%,#f6d6b0 0%,#c77a45 22%,#6e6a6c 50%,#3c4452 100%)}
.hero-shape{position:absolute;left:0;top:0}
.hero-title{position:absolute;left:100px;top:98px;font-family:"Source Sans 3",sans-serif;font-weight:700;font-size:44px;color:#fff;letter-spacing:.5px}
.hero-sub{position:absolute;left:100px;top:166px;font-family:"Source Sans 3",sans-serif;font-weight:300;font-size:38px;line-height:48px;color:#fff}
.hero-btn{position:absolute;left:100px;top:289px;width:196px;height:47px;border:2px solid #fff;color:#fff;font-family:"Source Sans 3",sans-serif;font-size:23px;padding:7px 16px}

/* feature cards */
.cards{position:absolute;left:99px;top:485px;width:1000px;height:317px;display:flex;gap:4px}
.card{width:248px;height:317px;background:#fff;box-shadow:0 4px 14px rgba(0,0,0,.16);padding:22px 22px 0}
.card-img{height:84px;margin-bottom:14px}
.card p{font-size:13px;line-height:17.5px;color:#222}
.card a{display:block;margin-top:12px;font-size:13px;font-weight:700;color:var(--link-blue);text-decoration:none}

/* audience band */
.audience{position:absolute;left:0;top:802px;width:1200px;height:292px;background:var(--sky);border-top:1px solid #d5e6ee;border-bottom:1px dotted #9fc9dc}
.tile{position:absolute;top:49px;width:283px;height:189px}
.tile-img{height:140px}
.tile-caption{height:49px;background:var(--red);color:#fff;font-family:"Source Sans 3",sans-serif;font-size:22px;display:flex;align-items:center;justify-content:space-between;padding:0 12px 0 16px}
.arrow-btn{width:36px;height:36px}

/* about */
.about-title{position:absolute;left:105px;top:1136px;font-family:"Source Sans 3",sans-serif;font-weight:400;font-size:44px;color:var(--red)}
.about-rule{position:absolute;left:105px;top:1197px;width:660px;height:1px;background:var(--line)}
.lead{position:absolute;left:103px;font-size:15px;color:var(--blue)}
.body-text{position:absolute;left:103px;width:660px;font-size:14px;line-height:22px;color:#222}
.ad-banner{position:absolute;left:850px;top:1147px;width:248px;height:249px;background:linear-gradient(120deg,#f0a030 0%,#3a7fb8 45%,#1b90c6 100%)}
.ad-text{position:absolute;right:18px;top:36px;text-align:right;font-family:"Source Sans 3",sans-serif;font-weight:600;font-size:20px;line-height:29px;color:#fff}
.ad-btn{position:absolute;right:16px;top:175px;background:var(--red);color:#fff;font-size:11px;font-weight:700;padding:6px 14px;border:1px solid #fff}
.sponsors{position:absolute;left:850px;top:1421px;width:249px;height:375px;border:1px solid #ccc;padding-top:24px}
.sponsor{width:135px;margin:0 auto 18px;background:#e9ecee;border-radius:3px}

/* corporate news */
.news-band{position:absolute;left:0;top:1827px;width:1200px;height:291px;background:var(--grey-band)}
.news-title{position:absolute;left:0;width:1200px;top:30px;text-align:center;font-family:"Questrial",sans-serif;font-weight:400;font-size:32px;color:var(--blue-dark)}
.news-lines{position:absolute;top:48px;height:10px;border-top:1px solid #bbb;border-bottom:1px solid #bbb}
.news-item{position:absolute;top:128px;width:460px}
.news-num{position:absolute;left:0;top:4px;width:45px;height:40px;border:1px solid #ddd;background:#fff;color:var(--red);font-size:22px;text-align:center;line-height:38px}
.news-head{margin-left:58px;font-weight:700;font-size:13.5px;line-height:19px;color:#333}
.news-body{margin-left:58px;margin-top:10px;font-size:12px;line-height:17.5px;color:var(--muted)}
.news-more{margin-left:58px;display:block;font-size:13px;font-weight:700;color:var(--blue-dark);text-decoration:none}
.news-divider{position:absolute;left:605px;top:105px;width:1px;height:160px;background:#ccc}

/* footer */
.site-footer{position:absolute;left:0;top:2118px;width:1200px;height:205px;background:linear-gradient(var(--footer-top),var(--footer-bottom));color:#fff}
.footer-col{position:absolute;top:34px}
.footer-col h4{font-family:"Source Sans 3",sans-serif;font-weight:700;font-size:19px;margin-bottom:14px}
.footer-col li{list-style:none;font-size:12px;line-height:23px;padding-left:2px}
.footer-brand{position:absolute;left:852px;top:30px;display:flex;align-items:center;gap:8px;font-family:"Source Sans 3",sans-serif;font-weight:700;font-size:26px}
.footer-brand span.dot{width:20px;height:20px;border-radius:50%;background:#fff}
.footer-copy{position:absolute;left:760px;top:104px;width:310px;text-align:center;font-size:12.5px;line-height:23px}
.social{position:absolute;left:835px;top:158px;display:flex;gap:10px}
.social span{width:26px;height:26px;border-radius:50%;background:#fff;display:block}
</style>
</head>
<body>

<header class="site-header">
  <div class="brand"><span class="brand-mark"></span>TKBÓ</div>
  <nav class="main-nav">
    <a class="current">HOME</a><a>NEWS</a><a>EDUCATION</a><a>LIBRARY</a><a>LOKALAVD</a><a>YOUNG STUD</a>
  </nav>
</header>

<section class="hero">
  <div class="hero-photo" role="img" aria-label="Photo of a welder in an orange jacket and welding helmet working with sparks"></div>
  <svg class="hero-shape" width="600" height="410" viewBox="0 0 600 410">
    <defs>
      <linearGradient id="heroBlue" x1="0" y1="0" x2="0" y2="1">
        <stop offset="0" stop-color="#2aa2d6"/><stop offset="1" stop-color="#0e6d9f"/>
      </linearGradient>
    </defs>
    <polygon points="0,0 388,0 500,236 420,410 0,410" fill="url(#heroBlue)"/>
    <polygon points="388,0 442,0 556,236 474,410 420,410 500,236" fill="#c4161c"/>
    <polygon points="442,0 452,0 566,236 484,410 474,410 556,236" fill="#fff" opacity=".85"/>
  </svg>
  <h1 class="hero-title">TKBÓ WELDING</h1>
  <p class="hero-sub">simply dummy text<br>of the printing</p>
  <div class="hero-btn">Read More...</div>
</section>

<section class="cards">
  <article class="card">
    <div class="card-img" role="img" aria-label="Welding sparks in a blue-lit workshop" style="background:linear-gradient(135deg,#1a2a5a,#5a7ac0 55%,#d8e2f6)"></div>
    <p>Lorem Ipsum is simply dummy text of the pring and typesetting industry. Lorem Ipsum has been the industry's standard.</p>
    <a>Readmore [+]</a>
  </article>
  <article class="card">
    <div class="card-img" role="img" aria-label="Welder silhouetted against a sunset sky" style="background:linear-gradient(#f2b21c,#d9621c 60%,#5a2a14)"></div>
    <p>Lorem Ipsum is simply dummy text of the pring and typesetting industry. Lorem Ipsum has been the industry's standard.</p>
    <a>Readmore [+]</a>
  </article>
  <article class="card" style="padding-top:28px">
    <div class="card-img" role="img" aria-label="Welder on a steel beam under a blue sky" style="background:linear-gradient(#2c8fd8,#5aaee6 70%,#5b4a3c)"></div>
    <p>Lorem Ipsum is simply dummy text of the pring and typesetting industry. Lorem Ipsum has been the industry's standard.</p>
    <a>Readmore [+]</a>
  </article>
  <article class="card" style="padding-top:28px">
    <div class="card-img" role="img" aria-label="Bright welding arc in a dark workshop" style="background:radial-gradient(circle at 50% 60%,#fff,#8ab8e6 25%,#1e2a44 70%)"></div>
    <p style="margin-top:8px">Lorem Ipsum is simply dummy text of the pring and typesetting industry. Lorem Ipsum has been the industry's standard.</p>
    <a>Readmore [+]</a>
  </article>
</section>

<section class="audience">
  <div class="tile" style="left:107px">
    <div class="tile-img" role="img" aria-label="Welder at work with sparks and blue light" style="background:radial-gradient(circle at 45% 40%,#e8f0ff,#4a6aa8 35%,#121c30 80%)"></div>
    <div class="tile-caption">Institutional Investors
      <svg class="arrow-btn" viewBox="0 0 36 36"><circle cx="18" cy="18" r="18" fill="#1d8fc4"/><path d="M9 18h16M19 11l7 7-7 7" stroke="#fff" stroke-width="3" fill="none"/></svg></div>
  </div>
  <div class="tile" style="left:460px">
    <div class="tile-img" role="img" aria-label="Grinding sparks spraying in a workshop" style="background:radial-gradient(circle at 55% 45%,#ffe9b0,#d48a2e 30%,#2a2e3a 80%)"></div>
    <div class="tile-caption">Wealthy Individuals
      <svg class="arrow-btn" viewBox="0 0 36 36"><circle cx="18" cy="18" r="18" fill="#1d8fc4"/><path d="M9 18h16M19 11l7 7-7 7" stroke="#fff" stroke-width="3" fill="none"/></svg></div>
  </div>
  <div class="tile" style="left:817px">
    <div class="tile-img" role="img" aria-label="Welder on a steel structure under a blue sky" style="background:linear-gradient(#2a8fd6,#5fb2e8 60%,#4a3d34)"></div>
    <div class="tile-caption">Family Offices
      <svg class="arrow-btn" viewBox="0 0 36 36"><circle cx="18" cy="18" r="18" fill="#1d8fc4"/><path d="M9 18h16M19 11l7 7-7 7" stroke="#fff" stroke-width="3" fill="none"/></svg></div>
  </div>
</section>

<main>
  <h2 class="about-title">About TKBÓ Welding</h2>
  <div class="about-rule"></div>
  <p class="lead" style="top:1234px">Ipsum has been the industry's standard dummy text ever since the 1500s,</p>
  <p class="body-text" style="top:1271px">Lorem Ipsum is simply dummy text of the printing and typesetting industry. Lorem Ipsum has been the industry's standard dummy text ever since the 1500s, when an unknown printer took a galley of type and scrambled it to make a type specimen book.</p>
  <p class="body-text" style="top:1359px">It has survived not only five centuries, but also the leap into electronic typesetting, remaining essentially unchanged. It was popularised in the 1960s with the release of Pressmark sheets containing Lorem Ipsum passages, and more recently with desktop publishing software like Folden LayoutDesk including versions of Lorem Ipsum.</p>
  <p class="body-text" style="top:1469px">When an unknown printer took a galley of type and scrambled it to make a type specimen book. It has survived not only five centuries, but also the leap into electronic typesetting, remaining essentially unchanged. It was popularised in the 1960s with the release of Pressmark sheets containing Lorem Ipsum passages, and more recently with desktop</p>
  <p class="lead" style="top:1607px;left:99px">Ipsum has been the industry's standard dummy text ever since the 1500s,</p>
  <p class="body-text" style="top:1642px;left:99px;width:680px">Lorem Ipsum is simply dummy text of the printing and typesetting industry. Lorem Ipsum has been the industry's standard dummy text ever since the 1500s, when an unknown printer took a galley of type and scrambled it to make a type specimen book.</p>

  <aside class="ad-banner" role="img" aria-label="Advertisement banner with a welder in a helmet">
    <div class="ad-text">Welding<br>&amp; Metal<br>working<br>industry</div>
    <div class="ad-btn">LEARN MORE</div>
  </aside>
  <aside class="sponsors">
    <div class="sponsor" style="height:62px"></div>
    <div class="sponsor" style="height:30px;width:125px"></div>
    <div class="sponsor" style="height:40px;width:125px"></div>
    <div class="sponsor" style="height:54px;width:125px"></div>
    <div class="sponsor" style="height:62px"></div>
  </aside>
</main>

<section class="news-band">
  <div class="news-lines" style="left:120px;width:365px"></div>
  <div class="news-lines" style="left:760px;width:312px"></div>
  <h2 class="news-title">Corporate News</h2>
  <article class="news-item" style="left:105px">
    <div class="news-num">01</div>
    <h3 class="news-head">LOREM IPSUM DOLOR SIT AMET CONSECTETUR ADIPISICING</h3>
    <p class="news-body">Sorrupti quos dolores etquas molestias exceptur sint occaecati cupificia deserunt mollitia animi id est laborum et dolorum fuga. Et harum quidem rerum facilisest et expedita distinctio.Sorrupti quos dolores etquas moles</p>
    <a class="news-more">read more...</a>
  </article>
  <div class="news-divider"></div>
  <article class="news-item" style="left:625px">
    <div class="news-num">02</div>
    <h3 class="news-head">LOREM IPSUM DOLOR SIT AMET CONSECTETUR ADIPISICING</h3>
    <p class="news-body">Sorrupti quos dolores etquas molestias exceptur sint occaecati cupificia deserunt mollitia animi id est laborum et dolorum fuga. Et harum quidem rerum facilisest et expedita distinctio.Sorrupti quos dolores etquas moles</p>
    <a class="news-more">read more...</a>
  </article>
</section>

<footer class="site-footer">
  <div class="footer-col" style="left:115px"><h4>WHO WE ARE</h4>
    <ul><li>Company</li><li>News</li><li>Team</li><li>Careers</li><li>Contact</li></ul></div>
  <div class="footer-col" style="left:300px"><h4>WHAT WE DO</h4>
    <ul><li>What is Vellor Trading ?</li><li>Live Demo</li><li>Resources</li><li>FAQs</li><li>Mobile Apps</li></ul></div>
  <div class="footer-col" style="left:511px"><h4>WHO WE WORK WITH</h4>
    <ul><li>Utilities</li><li>Consumers</li><li>Partners</li><li>Get Started</li></ul></div>
  <div class="footer-brand"><span class="dot"></span>TKBÓ</div>
  <p class="footer-copy">2006 - 2013 TKBÓ Islands Privacy Policy Terms of Conditions. All Rights Reserved</p>
  <div class="social"><span></span><span></span><span></span><span></span><span></span></div>
</footer>

</body>
</html>
```